BRIGHTWELL PROPERTY CHECKS Business card, please make it match the flyer.
Dana Kowalt
Dana@brightwellpropertychecksfl.example
352-555-0187 office
www.BrightwellPropertyChecks.example

Contact Information for Business Card

OUR LOGO

```html
<!DOCTYPE html>
<html lang="en">
<head>
<meta charset="utf-8">
<title>Brightwell Property Checks – Business Card</title>
<link href="https://fonts.googleapis.com/css2?family=Montserrat:wght@500;600&family=Oswald:wght@500;600;700&display=swap" rel="stylesheet">
<style>
  :root {
    --bg: #3a3a3c;
    --white: #ffffff;
    --red: #e3202a;
    --blue: #1f5fb4;
    --blue-dark: #184c93;
    --ink: #222222;
    --plate-dark: #141414;
    --plate-mid: #2a2a2a;
    --flag-soft: #f3dfe2;
    --flag-star: #e4e8f2;
  }
  * { box-sizing: border-box; margin: 0; padding: 0; }
  html, body { width: 1200px; height: 1200px; overflow: hidden; }
  body {
    background: var(--bg);
    display: flex; flex-direction: column; align-items: center; justify-content: center;
    gap: 56px;
    font-family: "Oswald", sans-serif;
  }
  .card {
    position: relative; width: 900px; height: 514px;
    border-radius: 34px; overflow: hidden;
    box-shadow: 0 12px 30px rgba(0,0,0,.45);
  }

  /* Front */
  .card-front { background: var(--white); }
  .flag-wave {
    position: absolute; left: 0; top: 0; width: 480px; height: 330px;
    background: linear-gradient(150deg, var(--flag-star) 0%, var(--flag-soft) 30%, rgba(255,255,255,0) 62%);
  }
  .brand {
    position: absolute; right: 60px; top: 70px;
    display: flex; align-items: center; gap: 14px;
  }
  .brand-mark { width: 40px; height: 40px; border-radius: 50%; background: var(--red); flex: none; }
  .brand-name {
    font-family: "Oswald", sans-serif; font-weight: 600; font-size: 30px;
    color: var(--blue-dark); line-height: 1.05; letter-spacing: .5px;
  }
  .identity { position: absolute; left: 56px; top: 118px; }
  .person-name {
    font-family: "Montserrat", sans-serif; font-weight: 600; font-size: 44px;
    color: var(--red); line-height: 1;
  }
  .person-role {
    font-family: "Montserrat", sans-serif; font-weight: 500; font-size: 20px;
    color: var(--ink); margin: 4px 0 0 10px;
  }
  .contact-list { list-style: none; margin: 10px 0 0 10px; }
  .contact-list li {
    display: flex; align-items: center; gap: 12px;
    font-family: "Oswald", sans-serif; font-weight: 500; font-size: 20px;
    color: var(--ink); text-transform: uppercase; line-height: 1.45;
    white-space: nowrap;
  }
  .contact-list svg { width: 20px; height: 20px; flex: none; }

  .services-title {
    position: absolute; right: 60px; top: 276px;
    font-family: "Oswald", sans-serif; font-weight: 600; font-size: 22px;
    color: var(--blue); letter-spacing: 2px;
  }
  .service-band {
    position: absolute; left: 0; bottom: 0; width: 100%; height: 190px;
    background: linear-gradient(180deg, var(--blue) 0%, var(--blue-dark) 100%);
  }
  .services {
    position: absolute; left: 0; bottom: 14px; width: 100%;
    display: flex; justify-content: space-around; padding: 0 20px;
  }
  .service { width: 130px; text-align: center; }
  .service-icon {
    width: 72px; height: 72px; margin: 0 auto 10px; border-radius: 50%;
    background: var(--red); border: 3px solid var(--white);
    display: flex; align-items: center; justify-content: center;
  }
  .service-icon svg { width: 36px; height: 36px; }
  .service-label {
    font-family: "Oswald", sans-serif; font-weight: 600; font-size: 17px;
    color: var(--white); text-transform: uppercase; line-height: 1.15;
  }

  /* Back */
  .card-back {
    background: radial-gradient(circle at 50% 45%, var(--plate-mid) 0%, var(--plate-dark) 80%);
    display: flex; align-items: center; justify-content: center;
  }
  .back-brand { display: flex; align-items: center; gap: 22px; }
  .back-brand .brand-mark { width: 64px; height: 64px; }
  .back-brand .brand-name { color: var(--white); font-size: 52px; }
</style>
</head>
<body>

<section class="card card-front">
  <div class="flag-wave" role="img" aria-label="Faint waving American flag in soft red, white and blue"></div>

  <div class="brand">
    <span class="brand-mark"></span>
    <span class="brand-name">BRIGHTWELL<br>PROPERTY CHECKS</span>
  </div>

  <div class="identity">
    <h1 class="person-name">Dana Kowalt</h1>
    <p class="person-role">OWNER</p>
    <ul class="contact-list">
      <li>
        <svg viewBox="0 0 24 24"><path fill="#e3202a" d="M6.6 10.8a15 15 0 0 0 6.6 6.6l2.2-2.2c.3-.3.7-.4 1-.2 1.1.4 2.3.6 3.6.6.6 0 1 .4 1 1V20c0 .6-.4 1-1 1A17 17 0 0 1 3 4c0-.6.4-1 1-1h3.5c.6 0 1 .4 1 1 0 1.3.2 2.5.6 3.6.1.3 0 .7-.2 1z"/></svg>
        352-555-0187
      </li>
      <li>
        <svg viewBox="0 0 24 24"><rect x="2" y="5" width="20" height="14" fill="#e3202a"/><path d="M2 5l10 8 10-8" fill="none" stroke="#fff" stroke-width="2"/></svg>
        Dana@brightwellpropertychecksfl.example
      </li>
      <li>
        <svg viewBox="0 0 24 24" fill="none" stroke="#e3202a" stroke-width="2"><circle cx="12" cy="12" r="9"/><path d="M3 12h18M12 3c3 3 3 15 0 18M12 3c-3 3-3 15 0 18"/></svg>
        www.BrightwellPropertyChecks.example
      </li>
    </ul>
  </div>

  <p class="services-title">OUR SERVICES</p>

  <div class="service-band"></div>
  <div class="services">
    <div class="service">
      <div class="service-icon"><svg viewBox="0 0 24 24" fill="#fff"><path d="M12 3l9 8h-3v9H6v-9H3z"/></svg></div>
      <p class="service-label">Home<br>Inspections</p>
    </div>
    <div class="service">
      <div class="service-icon"><svg viewBox="0 0 24 24" fill="#fff"><rect x="3" y="8" width="8" height="13"/><rect x="12" y="3" width="9" height="18"/></svg></div>
      <p class="service-label">Commercial<br>Inspections</p>
    </div>
    <div class="service">
      <div class="service-icon"><svg viewBox="0 0 24 24" fill="#fff"><path d="M4 12l8-8 8 8h-2v8H6v-8z"/><rect x="10" y="14" width="4" height="6" fill="#e3202a"/></svg></div>
      <p class="service-label">Pre-Listing<br>Inspections</p>
    </div>
    <div class="service">
      <div class="service-icon"><svg viewBox="0 0 24 24"><rect x="5" y="3" width="14" height="18" fill="#fff"/><path d="M8 8h8M8 12h8M8 16h5" stroke="#e3202a" stroke-width="2"/></svg></div>
      <p class="service-label">4-Point<br>Inspections</p>
    </div>
    <div class="service">
      <div class="service-icon"><svg viewBox="0 0 24 24" fill="#fff"><circle cx="8" cy="8" r="2.5"/><circle cx="16" cy="8" r="2.5"/><circle cx="8" cy="16" r="2.5"/><circle cx="16" cy="16" r="2.5"/></svg></div>
      <p class="service-label">Warranty<br>Inspections</p>
    </div>
    <div class="service">
      <div class="service-icon"><svg viewBox="0 0 24 24" fill="none" stroke="#fff" stroke-width="2" stroke-linecap="round"><path d="M3 8h12a3 3 0 1 0-3-3M3 12h16a3 3 0 1 1-3 3M3 16h8"/></svg></div>
      <p class="service-label">Wind<br>Mitigations</p>
    </div>
  </div>
</section>

<section class="card card-back" role="img" aria-label="Black diamond-plate metal texture behind the company name">
  <div class="back-brand">
    <span class="brand-mark"></span>
    <span class="brand-name">BRIGHTWELL<br>PROPERTY CHECKS</span>
  </div>
</section>

</body>
</html>
```